First Aid Training business needs business card design

We would like a double sided business card designed for a first aid training business - Brindlewood First Aid. We provide first aid training and , WHS (work, health and safety) training.

The attached word document contains the key information we would like on each side of the business card.

Final design needs to be delivered in print ready format, along with the original file.

```html
<!DOCTYPE html>
<html lang="en">
<head>
<meta charset="utf-8">
<title>Brindlewood First Aid – Business Cards</title>
<link rel="stylesheet" href="https://fonts.googleapis.com/css2?family=Montserrat:wght@600;700&family=Arimo:wght@400;700&display=swap">
<style>
  :root {
    --brand-red: #e8242a;
    --ink: #1a1a1a;
    --paper: #f7f7f7;
    --backdrop: #dcdcdc;
    --divider: #b5b5b5;
    --white: #ffffff;
  }
  * { box-sizing: border-box; margin: 0; padding: 0; }
  html, body {
    width: 1200px; height: 930px; overflow: hidden;
    background: var(--backdrop);
  }
  .sheet {
    width: 1200px; height: 930px;
    display: flex; flex-direction: column; align-items: center; justify-content: center;
    gap: 60px;
  }
  .card {
    position: relative;
    width: 640px; height: 366px;
    box-shadow: 0 6px 18px rgba(0,0,0,0.12);
  }
  .card--front { background: var(--paper); }
  .card--back { background: var(--brand-red); }

  .wordmark {
    position: absolute;
    display: flex; align-items: center; gap: 22px;
  }
  .wordmark__dot {
    width: 74px; height: 74px; border-radius: 50%;
    flex: none;
  }
  .wordmark__name {
    font-family: "Montserrat", sans-serif;
    font-weight: 700;
    line-height: 1.05;
    letter-spacing: 0.02em;
    text-transform: uppercase;
  }
  .wordmark__name .line-1 { display: block; font-size: 34px; }
  .wordmark__name .line-2 { display: block; font-size: 17px; letter-spacing: 0.06em; }

  .card--front .wordmark { left: 150px; top: 70px; }
  .card--front .wordmark__dot { background: var(--brand-red); }
  .card--front .wordmark__name { color: var(--ink); }

  .card--back .wordmark { left: 150px; top: 60px; }
  .card--back .wordmark__dot { background: var(--white); }
  .card--back .wordmark__name { color: var(--white); }

  .contact-block {
    position: absolute; left: 60px; bottom: 62px;
    display: flex; align-items: center;
  }
  .person-name {
    font-family: "Montserrat", sans-serif; font-weight: 700;
    font-size: 20px; color: var(--brand-red); letter-spacing: 0.03em;
    text-transform: uppercase;
    padding-right: 22px;
  }
  .contact-list {
    list-style: none;
    border-left: 1px solid var(--divider);
    padding-left: 18px;
    font-family: "Arimo", sans-serif; font-size: 15px; color: var(--ink);
    line-height: 1.45;
  }
  .contact-list li { display: flex; align-items: center; gap: 8px; }
  .contact-list svg { width: 13px; height: 13px; flex: none; }
  .contact-list .web { color: var(--brand-red); }
  .contact-list .web span { color: var(--ink); }

  .service-lines {
    position: absolute; left: 60px; right: 40px; top: 190px;
    font-family: "Arimo", sans-serif; color: var(--white);
    text-transform: none;
  }
  .service-lines p { font-size: 15px; line-height: 1.7; }
  .service-lines .headline { letter-spacing: 0.04em; }
</style>
</head>
<body>
<main class="sheet">

  <section class="card card--front" aria-label="Business card front">
    <div class="wordmark">
      <span class="wordmark__dot"></span>
      <span class="wordmark__name"><span class="line-1">Brindlewood</span><span class="line-2">First Aid Training</span></span>
    </div>

    <div class="contact-block">
      <p class="person-name">Daniel Marsh</p>
      <ul class="contact-list">
        <li>
          <svg viewBox="0 0 24 24" aria-hidden="true"><path fill="#e8242a" d="M6.6 10.8a15.1 15.1 0 0 0 6.6 6.6l2.2-2.2a1 1 0 0 1 1-.25 11.4 11.4 0 0 0 3.6.57 1 1 0 0 1 1 1V20a1 1 0 0 1-1 1A17 17 0 0 1 3 4a1 1 0 0 1 1-1h3.5a1 1 0 0 1 1 1c0 1.25.2 2.45.57 3.57a1 1 0 0 1-.25 1z"/></svg>
          0412 836 590
        </li>
        <li>
          <svg viewBox="0 0 24 24" aria-hidden="true"><rect x="2" y="5" width="20" height="14" fill="#e8242a"/><path d="M2 5l10 8 10-8" fill="none" stroke="#fff" stroke-width="2"/></svg>
          help@brindlewoodfirstaid.com.au
        </li>
        <li class="web">
          <svg viewBox="0 0 24 24" aria-hidden="true"><circle cx="12" cy="12" r="10" fill="none" stroke="#e8242a" stroke-width="2"/><path d="M2 12h20M12 2c3 3 3 17 0 20M12 2c-3 3-3 17 0 20" fill="none" stroke="#e8242a" stroke-width="1.6"/></svg>
          brindlewoodfirstaid<span>.com.au</span>
        </li>
      </ul>
    </div>
  </section>

  <section class="card card--back" aria-label="Business card back">
    <div class="wordmark">
      <span class="wordmark__dot"></span>
      <span class="wordmark__name"><span class="line-1">Brindlewood</span><span class="line-2">First Aid Training</span></span>
    </div>

    <div class="service-lines">
      <p class="headline">ONSITE TRAINING – WE CAN COME TO YOU</p>
      <p>•Time efficient &nbsp;• Cost effective • Minimise downtime for your team</p>
      <p class="headline">FIRST AID TRAINING &nbsp;| WHS TRAINING</p>
    </div>
  </section>

</main>
</body>
</html>
```